Hoofcare business card

I would like to create a business card design for my hoofcare business.

Front Side- would like to just include the logo and text as per the uploaded files- text font to match logo (upper and lower case).

Back side
- Include the details and contact information provided on the uploaded file.
- Also included on the back side- the uploaded TRUMV logo- keep it small on a top or bottom corner
- for facebook and Instagram contacts- please use the logos next to my usernames

```html
<!DOCTYPE html>
<html lang="en">
<head>
<meta charset="utf-8">
<title>Kestrel Equine Hoofcare – Business Cards</title>
<link href="https://fonts.googleapis.com/css2?family=Roboto:wght@400;700&display=swap" rel="stylesheet">
<style>
  :root {
    --backdrop-light: #d4d4d4;
    --backdrop-dark: #a9a9a9;
    --card: #2a2a2a;
    --card-edge: #232323;
    --ink: #ffffff;
    --ink-soft: #e6e6e6;
    --deco-light: #4a4a4a;
    --deco-dark: #2e2e2e;
    --badge: #f2f2f2;
  }
  * { box-sizing: border-box; margin: 0; padding: 0; }
  html, body { width: 1200px; height: 788px; overflow: hidden; }
  body {
    font-family: "Roboto", Arial, sans-serif;
    background: linear-gradient(160deg, var(--backdrop-light), var(--backdrop-dark));
    display: flex;
    align-items: center;
    justify-content: center;
    gap: 50px;
  }
  .card {
    position: relative;
    width: 540px;
    height: 320px;
    background: var(--card);
    border-radius: 22px;
    box-shadow: 0 18px 40px rgba(0,0,0,.35);
    color: var(--ink);
    overflow: hidden;
  }

  /* Back side */
  .back .horse-mark {
    position: absolute;
    right: 70px;
    top: -10px;
    width: 230px;
    height: 240px;
    border-radius: 40% 50% 30% 40%;
    background: radial-gradient(ellipse at 40% 30%, var(--deco-light), var(--deco-dark) 70%);
    opacity: .8;
  }
  .back .cert-badge {
    position: absolute;
    right: 28px;
    top: 60px;
    width: 50px;
    height: 50px;
    border-radius: 50%;
    background: var(--badge);
  }
  .back .details {
    position: absolute;
    left: 38px;
    bottom: 34px;
  }
  .back .credential {
    font-weight: 700;
    font-size: 17px;
    letter-spacing: .3px;
    margin-bottom: 4px;
  }
  .back .service {
    font-size: 14px;
    line-height: 1.35;
    color: var(--ink-soft);
    margin-bottom: 22px;
  }
  .back .name {
    font-weight: 700;
    font-size: 25px;
    letter-spacing: .5px;
    margin-bottom: 10px;
  }
  .contact-list { list-style: none; font-size: 14px; line-height: 1.45; color: var(--ink-soft); }
  .contact-list li { display: flex; align-items: center; gap: 8px; }
  .contact-list svg { width: 13px; height: 13px; flex: none; }
  .dot { width: 12px; height: 12px; border-radius: 50%; background: var(--ink-soft); flex: none; }

  /* Front side */
  .front { display: flex; flex-direction: column; align-items: center; justify-content: center; }
  .front .brand {
    display: flex;
    align-items: center;
    gap: 12px;
    font-size: 34px;
    font-weight: 400;
    margin-bottom: 44px;
  }
  .front .brand-dot { width: 14px; height: 14px; border-radius: 50%; background: var(--ink); }
  .front .tagline {
    text-align: center;
    font-weight: 700;
    font-size: 19px;
    line-height: 1.3;
  }
</style>
</head>
<body>
  <section class="card back">
    <div class="horse-mark" role="img" aria-label="Large faint horse head emblem decoration"></div>
    <div class="cert-badge" aria-hidden="true"></div>
    <div class="details">
      <p class="credential">TRUMV TRAINED BAREFOOT TRIMMER</p>
      <p class="service">Equine Barefoot Trimming and Rehabilitation<br>for all horses, ponies and donkeys</p>
      <p class="name">HARRIET VANCE</p>
      <ul class="contact-list">
        <li>
          <svg viewBox="0 0 12 12" aria-hidden="true"><rect x="3" y="0.5" width="6" height="11" rx="1.2" fill="none" stroke="currentColor"/><circle cx="6" cy="9.6" r=".7" fill="currentColor"/></svg>
          0400 555 019
        </li>
        <li>
          <svg viewBox="0 0 12 12" aria-hidden="true"><rect x=".5" y="2.5" width="11" height="7" fill="none" stroke="currentColor"/><path d="M.5 2.5 6 7l5.5-4.5" fill="none" stroke="currentColor"/></svg>
          kestrelhoofcare@mailbox.com
        </li>
        <li><span class="dot"></span>Kestrel Equine Hoofcare</li>
        <li><span class="dot"></span>kestrelhoofcare</li>
      </ul>
    </div>
  </section>

  <section class="card front">
    <div class="brand"><span class="brand-dot"></span>Kestrel Equine Hoofcare</div>
    <p class="tagline">Equine Barefoot Trimming and Rehabilitation<br>Harlow Bay and Surrounds</p>
  </section>
</body>
</html>
```